financial company web page

We are tax and financial consulting company that needs a web site. Our logo is attached. Headquarters of our company is based in Latvia, Riga. Our actual temporary web site is www.norquill.com The main purpose of our new web site is:
* to explain the benefits of doing business through Latvian LLC companies;
* provide necessary information about taxation regime in Latvia for trading and holding companies
* propose some standard schemes of using Latvian companies for various businesses.
* offer our clients other jurisdictions companies - other European, offshore, etc.
* offer our clients ecommerce solutions
* offer our client residency in Latvia and EU
Registration of a Latvian company + accounting + legal advice will be our primary product. However, web site first page should highlight 4 other important products, such as:
1 - eCommerce (here we will explain briefly what is eCommerce, how our client can use it, what are the bonuses doing business online, explain conditions of eCommerce, etc) ;
2 - Residence Permit (here we offer EU and non-EU citizens to obtain Latvian residence permit and explain the benefits of having Latvian ID card);
3 - other Jurisdictions (here we propose list of other companies registered in the countries with favorable taxation regime, i.e. UK, Hong-Kong, Canada, Panama, BVI, UAE, etc);
4 - banking (here we explain benefits of having bank account in Latvia, explaining briefly products that bank offer, etc).
Overall Website map is the following:
1. About us
2. About Latvia
3. Contacts
4. Latvian company
5. Our services
a. еCommerce
b. Resident permit (Latvia and EU)
c. Bank accounts
d. Registration and support of other jurisdictions (European companies, Low tax companies, Offshore companies)
e. Additional services (Tax advisory, Virtual office, European licenses, Accounting services, Legal address in Riga)
6. Become Partner
7. Tembrole Travel Guide
As a start point we need only first page design. If this design suits us well we will continue to work with you on other pages. We are looking for innovative, creative and professional design in line with our corporate logo and colours. We want this design to focus more on graphic, on simplicity and usability. It should be immediately clear from the first glance what the site is about, what is our key product and how to get more information if I'm interested on something.
These are website from our sector, we want to be better:
http://www.vantel-ridge.com/
http://www.qpr-harbourline.com/
http://www.dxlventurebuilders.com/
http://www.firmstarter318.co.uk/
In case you can't find our logo, please, ask I will send it to your mail. Thanks!
Target Market(s)
European, Russian or Chinesee enterpreneurs
Industry/Entity Type
Accounting
Requirements
Must have
- Web site will be on 10 languages, so somewhere must be a button/flag to switch language.
Contact information should be on every page (phone number and add Skype buttons or similar).
Search button should be available on the first page
Button Request a Call should be on every page.
Visitors should also have a possibility to download a brochure about each product (so appropriate button should be in each section).

```html
<!DOCTYPE html>
<html lang="en">
<head>
<meta charset="utf-8">
<title>Tembrole — Tax and Financial Solutions</title>
<link href="https://fonts.googleapis.com/css2?family=Signika:wght@400;600&family=Philosopher&family=Oswald:wght@500&family=Libre+Baskerville:ital@0;1&family=Open+Sans:ital,wght@0,400;0,600;1,700&display=swap" rel="stylesheet">
<style>
:root{
  --brand:#123f8f;
  --brand-bright:#1d63c4;
  --brand-deep:#0b3680;
  --link:#1155a8;
  --ink:#333;
  --muted:#666;
  --panel:#f3f3f3;
  --nav-top:#444;
  --nav-bottom:#1f1f1f;
  --line:#bbb;
  --white:#fff;
}
*{box-sizing:border-box;margin:0;padding:0}
html,body{width:878px;height:1200px;overflow:hidden;background:var(--white)}
body{position:relative;font-family:Arial,Helvetica,sans-serif;color:var(--ink)}
.abs{position:absolute}
a{color:inherit;text-decoration:none}

/* header */
.utility{top:8px;right:75px;font-size:10px;color:#222;display:flex;gap:17px}
.brand{top:30px;left:74px;display:flex;align-items:center;gap:10px}
.brand-mark{width:22px;height:22px;border-radius:50%;background:var(--brand)}
.brand-name{font-family:"Signika",sans-serif;font-weight:600;font-size:38px;color:var(--brand);letter-spacing:1px}
.phone{top:69px;left:629px;display:flex;align-items:center;gap:8px}
.phone-number{font-family:"Oswald",sans-serif;font-weight:500;font-size:24px;color:#444;letter-spacing:1px}

/* nav */
.main-nav{top:106px;left:0;width:878px;height:34px;background:linear-gradient(#4a4a4a,var(--nav-bottom))}
.main-nav ul{list-style:none;position:absolute;left:86px;top:0;height:34px;display:flex;align-items:center}
.main-nav li{font-size:10.4px;color:var(--white);padding:0 10.5px;line-height:24px;white-space:nowrap}
.main-nav li.active{background:#111;border:1px solid #666;border-radius:4px;padding:0 7px}

/* hero */
.hero-band{top:140px;left:0;width:878px;height:270px;background:linear-gradient(var(--brand-bright),var(--brand-deep))}
.slider{top:156px;left:97px;width:689px;height:286px;background:linear-gradient(#fafafa,#e8e8e8);border-radius:14px;box-shadow:0 8px 10px -6px rgba(0,0,0,.35)}
.slider-inner{top:18px;left:18px;width:653px;height:250px;background:var(--white);border-radius:10px}
.slide{top:183px;left:125px;width:635px;height:233px;border-radius:8px;background:radial-gradient(circle at 140px 100px,#1a6fc4 0,#6aa6dc 55px,#cfe2f2 110px,#e4eef7 220px,#eef4fa 100%)}
.slide-title{top:222px;left:380px;font-family:"Libre Baskerville",serif;font-size:33px;color:#111;line-height:1}
.slide-sub{top:255px;left:452px;font-family:"Libre Baskerville",serif;font-style:italic;font-size:24px;color:#111}
.slide-arrow{top:287px;width:37px;height:31px;background:linear-gradient(#444,#111);display:flex;align-items:center;justify-content:center}
.slide-arrow.prev{left:106px;border-radius:6px 16px 16px 6px}
.slide-arrow.next{left:740px;border-radius:16px 6px 6px 16px}
.read-details{top:374px;left:638px;width:104px;height:28px;background:linear-gradient(#555,#1a1a1a);border-radius:14px;display:flex;align-items:center;padding-left:9px;font-family:"Open Sans",sans-serif;font-weight:600;font-size:10px;color:var(--white)}
.read-details span.ring{position:absolute;right:0;top:0;width:28px;height:28px;border-radius:50%;background:linear-gradient(#666,#222);border:2px solid #ddd;display:flex;align-items:center;justify-content:center}
.slider-dots{top:410px;left:402px;width:80px;height:21px;background:linear-gradient(#fff,#ddd);border:1px solid #ccc;border-radius:11px;display:flex;align-items:center;justify-content:center;gap:3px}
.slider-dots i{width:7px;height:7px;border-radius:50%;background:#555}
.slider-dots i.on{background:var(--white);border:1px solid #555}

/* product columns */
.product{top:480px;width:152px}
.product h3{font-family:"Signika",sans-serif;font-weight:600;font-size:13.5px;color:var(--brand);height:22px}
.product .frame{width:152px;height:94px;border:1px solid #bbb;background:#f4f4f4;padding:5px;box-shadow:0 7px 6px -5px rgba(0,0,0,.35)}
.product .photo{width:100%;height:100%}
.product p{margin-top:17px;font-size:9.3px;line-height:13.2px;color:var(--ink)}
.product .more{display:block;text-align:right;margin-top:8px;font-size:9.6px;color:var(--link)}
.more::after{content:"";display:inline-block;margin-left:6px;border-left:3px solid var(--link);border-top:3px solid transparent;border-bottom:3px solid transparent}
.rule{left:76px;width:726px;border-top:1px dotted #999}

/* why us */
.why{top:736px;left:78px;width:722px;height:212px;background:var(--panel)}
.why-title{top:748px;left:88px;font-family:"Philosopher",sans-serif;font-size:18px;color:#333}
.why-item{left:91px;display:flex;gap:10px}
.why-item .thumb{width:45px;height:38px}
.why-item h4{font-family:"Open Sans",sans-serif;font-style:italic;font-weight:700;font-size:8.3px;color:var(--link);margin-left:2px}
.why-item p{font-family:"Open Sans",sans-serif;font-size:8.6px;line-height:12px;color:#222;width:215px}
.why-divider{left:414px;top:752px;height:178px;border-left:1px dotted #999}
.pager{top:927px;left:371px;display:flex;gap:2px}
.video{left:429px;display:flex;gap:13px}
.video .frame{width:117px;height:69px;border:1px solid #ccc;background:var(--white);padding:4px}
.video .photo{width:100%;height:100%}
.video h4{font-family:Arial,sans-serif;font-weight:400;font-size:12.6px;color:#333;margin:2px 0 7px 1px}
.video p{font-size:9.4px;line-height:14.4px;color:#555;width:244px}
.video a{font-size:9.4px;color:var(--link)}

/* footer info */
.info{top:978px;left:0;width:878px;height:168px;background:var(--panel)}
.info-rule{top:978px;left:77px;width:726px;border-top:1px dotted #999}
.col-title{font-family:"Philosopher",sans-serif;font-size:15.5px;color:var(--brand)}
.news h5{font-family:"Open Sans",sans-serif;font-weight:600;font-size:9.6px;color:#333;margin-top:10px}
.news p{font-family:"Open Sans",sans-serif;font-size:8.4px;line-height:13px;color:#777;margin-left:2px;width:205px}
.news time{display:block;font-family:"Open Sans",sans-serif;font-size:8.4px;color:var(--brand);margin:1px 0 -2px 2px}
.address p{font-size:8.8px;font-style:italic;line-height:17.5px;color:#333}
.address p.link{color:var(--link)}
.col-divider{top:1000px;height:128px;border-left:1px solid #ccc}
.email-field{top:1023px;left:559px;width:165px;height:25px;border-radius:13px;background:var(--white);box-shadow:inset 0 1px 3px rgba(0,0,0,.2);font-size:8.8px;color:#777;padding:7px 0 0 11px}
.newsletter-note{top:1059px;left:570px;width:210px;font-size:8.8px;line-height:17.5px;color:#333}

.site-foot{top:1146px;left:0;width:878px;height:54px;background:var(--brand-deep);color:var(--white);text-align:center;font-size:9.6px;font-weight:bold;line-height:17.6px;padding-top:9px}
</style>
</head>
<body>

<header>
  <nav class="abs utility"><a>Help</a><span>|</span><a>Login</a><span>|</span><a>Signup</a></nav>
  <div class="abs brand"><span class="brand-mark"></span><span class="brand-name">TEMBROLE</span></div>
  <div class="abs phone">
    <svg width="34" height="34" viewBox="0 0 34 34" aria-hidden="true">
      <circle cx="17" cy="17" r="15.5" fill="#fff" stroke="#1f3fb5" stroke-width="2.2"/>
      <path d="M11 9.5c1-1 2-1 2.6 0l1.8 3c.5.8.2 1.5-.5 2l-1 .8c.8 2 2.4 3.6 4.4 4.4l.8-1c.5-.7 1.2-1 2-.5l3 1.8c1 .6 1 1.6 0 2.6l-1.3 1.3c-1.3 1.3-4.8.5-8.4-3.1S8.4 12.1 9.7 10.8z" fill="#1f3fb5"/>
    </svg>
    <span class="phone-number">418 620 5173</span>
  </div>
</header>

<nav class="abs main-nav">
  <ul>
    <li class="active">ABOUT US</li><li>ABOUT LATVIA</li><li>OUR SERVICES</li><li>BLATVIAN COMPANY</li><li>CONTACTS</li><li>BECOME PARTNER</li><li>TEMBROLE TRAVEL GUIDE</li>
  </ul>
</nav>

<section aria-label="Featured slider">
  <div class="abs hero-band"></div>
  <div class="abs slider"><div class="abs slider-inner"></div></div>
  <div class="abs slide" role="img" aria-label="Glass globe resting on financial charts and paperwork"></div>
  <div class="abs slide-title">Financial</div>
  <div class="abs slide-sub">Investment</div>
  <div class="abs slide-arrow prev"><svg width="10" height="12" viewBox="0 0 10 12"><path d="M2 1l6 5-6 5" fill="none" stroke="#fff" stroke-width="2.4"/></svg></div>
  <div class="abs slide-arrow next"><svg width="10" height="12" viewBox="0 0 10 12"><path d="M8 1L2 6l6 5" fill="none" stroke="#fff" stroke-width="2.4"/></svg></div>
  <a class="abs read-details">Read Details<span class="ring"><svg width="9" height="12" viewBox="0 0 9 12"><path d="M1 0l8 6-8 6z" fill="#fff"/></svg></span></a>
  <div class="abs slider-dots"><i class="on"></i><i></i><i></i><i></i><i></i></div>
</section>

<section aria-label="Products">
  <article class="abs product" style="left:96px">
    <h3>New to investing?</h3>
    <div class="frame"><div class="photo" role="img" aria-label="Golden key and pocket watch on an investing page" style="background:linear-gradient(135deg,#e8e4dc,#b9a57a 55%,#8d8a84)"></div></div>
    <p>Lorem Ipsum is simply dummy text of the printing and typesetting industry. Lorem Ipsum has been the industry's standard dummy text.....</p>
    <a class="more">More information</a>
  </article>
  <article class="abs product" style="left:274px">
    <h3>Experienced investor?</h3>
    <div class="frame"><div class="photo" role="img" aria-label="Business colleagues working at a laptop" style="background:linear-gradient(135deg,#cfd6dc,#6f7780 50%,#e2e6ea)"></div></div>
    <p>Lorem Ipsum is simply dummy text of the printing and typesetting industry. Lorem Ipsum has been the industry's standard dummy text.....</p>
    <a class="more">More information</a>
  </article>
  <article class="abs product" style="left:453px">
    <h3>Investment guides</h3>
    <div class="frame"><div class="photo" role="img" aria-label="Hand handing over a set of keys" style="background:linear-gradient(135deg,#8a2a22,#c9a08a 50%,#3a2a28)"></div></div>
    <p>Lorem Ipsum is simply dummy text of the printing and typesetting industry. Lorem Ipsum has been the industry's standard dummy text.....</p>
    <a class="more">More information</a>
  </article>
  <article class="abs product" style="left:631px">
    <h3>investment ISA?</h3>
    <div class="frame"><div class="photo" role="img" aria-label="Stacks of coins on letter tiles spelling a savings word" style="background:linear-gradient(135deg,#b0201c,#c8a050 50%,#2a3a8a)"></div></div>
    <p>Lorem Ipsum is simply dummy text of the printing and typesetting industry. Lorem Ipsum has been the industry's standard dummy text.....</p>
    <a class="more">More information</a>
  </article>
</section>

<div class="abs rule" style="top:710px"></div>

<section aria-label="Why choose us">
  <div class="abs why"></div>
  <h2 class="abs why-title">Why Choese Us</h2>
  <div class="abs why-item" style="top:782px"><div class="thumb" role="img" aria-label="Team of business people" style="background:linear-gradient(#eef0f2,#8a8a8a)"></div><div><h4>Lorem ipsum dolor sit amet,</h4><p>Nam nibh. Nunc varius facilisis eros. Sed erat. In in velit quis arcu ornare laoreet.</p></div></div>
  <div class="abs why-item" style="top:835px"><div class="thumb" role="img" aria-label="Person reviewing paperwork" style="background:linear-gradient(#d9c3a8,#7a6a5a)"></div><div><h4>Lorem ipsum dolor sit amet,</h4><p>Nam nibh. Nunc varius facilisis eros. Sed erat. In in velit quis arcu ornare laoreet.</p></div></div>
  <div class="abs why-item" style="top:889px"><div class="thumb" role="img" aria-label="Group of smiling people" style="background:linear-gradient(#c89a6a,#4a4a5a)"></div><div><h4>Lorem ipsum dolor sit amet,</h4><p>Nam nibh. Nunc varius facilisis eros. Sed erat. In in velit quis arcu ornare laoreet.</p></div></div>
  <div class="abs pager">
    <svg width="12" height="12" viewBox="0 0 12 12"><circle cx="6" cy="6" r="5.3" fill="#fff" stroke="#333"/><path d="M7.5 3.5L4 6l3.5 2.5z" fill="#333"/></svg>
    <svg width="12" height="12" viewBox="0 0 12 12"><circle cx="6" cy="6" r="5.3" fill="#fff" stroke="#333"/><path d="M4.5 3.5L8 6 4.5 8.5z" fill="#333"/></svg>
  </div>
  <div class="abs why-divider"></div>
  <article class="abs video" style="top:758px">
    <div class="frame"><div class="photo" role="img" aria-label="Bright modern office with two people by the window" style="background:linear-gradient(135deg,#e6eaee,#5a6470 55%,#c9cfd5)"></div></div>
    <div><h4>Theme Custom Colors Demo Video</h4><p>Lorem ipsum dolor sit amet, consectetuer a iscing elit. Aenean commodo ligula eget dolo. Aenean massa. Cum sociis natoque penatibet</p><a>Read more...</a></div>
  </article>
  <article class="abs video" style="top:854px">
    <div class="frame"><div class="photo" role="img" aria-label="Hands holding a pen over a laptop" style="background:linear-gradient(135deg,#1a2a4a,#6a86a8 55%,#d8dde4)"></div></div>
    <div><h4>Theme Fonts Demo Video</h4><p>Lorem ipsum dolor sit amet, consectetuer a iscing elit. Aenean commodo ligula eget dolo. Aenean massa. Cum sociis natoque penatibet</p><a>Read more...</a></div>
  </article>
</section>

<section aria-label="Site information">
  <div class="abs info"></div>
  <div class="abs info-rule"></div>
  <div class="abs news" style="top:987px;left:82px">
    <h3 class="col-title">Latest news</h3>
    <h5>Theme Custom Colors Demo Video</h5>
    <p>Lorem ipsum dolor sit amet, consectetuer a iscing elit. Aenean commodo ligula eget dolo.</p>
    <time>September 4th, 2010</time>
    <h5>Theme Custom Colors Demo Video</h5>
    <p>Lorem ipsum dolor sit amet, consectetuer a iscing elit. Aenean commodo ligula eget dolo.</p>
    <time>September 4th, 2010</time>
  </div>
  <div class="abs col-divider" style="left:300px"></div>
  <div class="abs address" style="top:987px;left:321px">
    <h3 class="col-title" style="margin-bottom:6px">Address</h3>
    <p>321 Street Name,</p><p>UK, London</p><p>Phone: (1800) 765-4321</p><p>Fax: (1800) 765-4321</p>
    <p class="link">Website: http://yoursitename.com</p><p class="link">Email: info@yoursitename.com</p>
  </div>
  <div class="abs col-divider" style="left:513px"></div>
  <h3 class="abs col-title" style="top:988px;left:558px">Sign up for Newsletter</h3>
  <div class="abs email-field">Your email address...</div>
  <p class="abs newsletter-note">Cum sociis natoque penatibus et magnis dis parturient montes, nascetur ridiculus mus.</p>
</section>

<footer class="abs site-foot">
  © 2011 Tembroletaxandfinancialsolution. is proudly powered by PressLeaf | Entries (RSS) | Comments (RSS)<br>
  Privacy Statement Copyright Contact Us Site Map
</footer>

</body>
</html>
```